Business Card Design for a Lending Business (Hard Money loans)

We need a business card for our Real Estate Lending business. We do hard Money loans for real estate investors. We have an existing logo we like, see attached. I'd like the business card to mostly include the logo colors, but a bright color pop of some sort would be nice to see also. Card should include Logo, Company Name, Company Address, Employee Name, Cell Phone, Main Phone, Email, Website

Industry/Entity Type

Finance / Lending

Contact Information for Business Card

Logo, Company Name, Company Address, Employee Name, Cell Phone, Main Phone, Email, Website

Requirements
Nice to have
• I'd like the business card to mostly include the logo colors, but a bright color pop of some sort would be nice to see also.

```html
<!DOCTYPE html>
<html lang="en">
<head>
<meta charset="utf-8">
<title>Harbor Gate Lending – Business Card</title>
<link href="https://fonts.googleapis.com/css2?family=Arimo:wght@400;700&display=swap" rel="stylesheet">
<style>
  :root {
    --navy: #15308f;
    --cyan: #1aa7dc;
    --paper: #f6f6f4;
    --ink-light: #ffffff;
    --backdrop: #e8e8e8;
  }
  * { margin: 0; padding: 0; box-sizing: border-box; }
  html, body {
    width: 1200px; height: 853px; overflow: hidden;
    background: var(--backdrop);
    font-family: "Arimo", Arial, sans-serif;
  }
  .sheet {
    position: relative; width: 1200px; height: 853px;
    display: flex; align-items: center; justify-content: center; gap: 40px;
  }
  .card {
    position: relative; width: 540px; height: 309px;
    background: var(--paper); border-radius: 18px; overflow: hidden;
    box-shadow: 0 6px 18px rgba(0,0,0,0.12);
  }
  .card__panel { position: absolute; inset: 0; width: 100%; height: 100%; }
  .card__panel path { fill: var(--navy); }
  .contact {
    position: absolute; left: 38px; top: 38px; color: var(--ink-light);
  }
  .contact__name {
    color: var(--cyan); font-weight: 700; font-size: 17px;
    letter-spacing: 0.3px; text-transform: uppercase;
  }
  .contact__title { font-size: 12px; margin-top: 4px; }
  .contact__address { font-size: 12px; line-height: 1.4; margin-top: 74px; }
  .contact__list { list-style: none; margin-top: 8px; font-size: 12px; line-height: 1.45; }
  .contact__list li { display: flex; align-items: center; gap: 7px; }
  .contact__list svg { width: 11px; height: 11px; flex: none; }
  .contact__list svg * { stroke: var(--cyan); fill: none; stroke-width: 1.4; }
  .brand {
    position: absolute; display: flex; align-items: center; gap: 10px;
    color: var(--navy); font-weight: 700; letter-spacing: 1.5px;
    text-transform: uppercase; line-height: 1.15;
  }
  .brand__dot { border-radius: 50%; background: var(--cyan); flex: none; }
  .card--front .brand { left: 330px; top: 196px; font-size: 16px; }
  .card--front .brand__dot { width: 22px; height: 22px; }
  .card--back .brand { left: 50%; top: 50%; transform: translate(-50%, -50%); font-size: 20px; }
  .card--back .brand__dot { width: 28px; height: 28px; }
</style>
</head>
<body>
<main class="sheet">
  <section class="card card--front" aria-label="Business card front">
    <svg class="card__panel" viewBox="0 0 540 309" preserveAspectRatio="none" aria-hidden="true">
      <path d="M0,0 H290 C360,0 372,90 350,150 C330,205 300,255 250,309 H0 Z"/>
    </svg>
    <div class="contact">
      <p class="contact__name">Marissa Kowalczyk</p>
      <p class="contact__title">Loan Coordinator</p>
      <p class="contact__address">1250 Linden Hollow Road<br>Fallston, MD 21047</p>
      <ul class="contact__list">
        <li><svg viewBox="0 0 12 12"><path d="M3 1 L4.5 3.5 L3.5 4.8 C4.2 6.4 5.6 7.8 7.2 8.5 L8.5 7.5 L11 9 L10 11 C5.5 11 1 6.5 1 2 Z"/></svg>410-555-0142</li>
        <li><svg viewBox="0 0 12 12"><rect x="1" y="2.5" width="10" height="7"/><path d="M1 2.5 L6 6.5 L11 2.5"/></svg>info@HarborGateLending.com</li>
        <li><svg viewBox="0 0 12 12"><circle cx="6" cy="6" r="5"/><ellipse cx="6" cy="6" rx="2.2" ry="5"/><path d="M1 6 H11"/></svg>www.HarborGateLending.com</li>
      </ul>
    </div>
    <div class="brand"><span class="brand__dot"></span><span>Harbor Gate<br>Lending</span></div>
  </section>

  <section class="card card--back" aria-label="Business card back">
    <div class="brand"><span class="brand__dot"></span><span>Harbor Gate<br>Lending</span></div>
  </section>
</main>
</body>
</html>
```